Brightwell Course

Take the information and positional images that I have supplied (in the inDesign doc) and design a contemporary clean corporate brochure better than supplied. I would like an indesign or layered photoshop file back so that I can place the highres images in when I have finished and also the contact details when I get a number (not supplied) yet. I would like to use prussian blue and match it to other material that I am having made.

I'd like the design to be strong and dynamic as it is the first print run and will need sever other design concepts to compliment it. When one great and unique design comes through I am start with other brochures that fit in with it.

Its tailored to HR managers, but its an arts based training program so an element of visual sophistication would be advantageous.
Updates

Hi ........It will be printed on a matt eco/recycled card (which will absorb a lot of ink and be somewhat flat)

Dear Designers I am uploading some high res images to use in the layout which will be A5 6 page foldout. Thanks, have a great day!

Hi Designers, the design should be more than, and potentially different to what I supplied. It can be similar but I am actually looking for a more sophisticated design than what I suppled. Thank you.

Hi Designers, thanks so much for your designs so far. My feeling is that I may have confused the brief, I would prefer if the design was not the same as mine, the reason I have submitted my design to ArtHive is so that I could have a different design. This brochure will go out to 3000 people so I want it to look strong and sophisticated. I am also going to create 4-5 other designs from this one to go in packs, so this design (its my first time with ArtHive) needs to be strong so that everything else can be moulded against it. I haven't submitted the other briefs yet as it would be a waste of time until the first one is done. Thank you kindly.

Target Market(s)

Corporates & HR Managers

Industry/Entity Type

Training

Requirements
Must have
• Logo and prussian blue as a colour. An inDesign (CS5) file returned so I can drop hi res positionals in at a later stage.
Should not have
• Flattened files as details for this brochure are not finalised

```html
<!DOCTYPE html>
<html lang="en">
<head>
<meta charset="utf-8">
<title>Brightwell Course – Team Quote Panel</title>
<link href="https://fonts.googleapis.com/css2?family=Crimson+Text:ital,wght@0,700;1,400&family=Raleway:wght@300;400&display=swap" rel="stylesheet">
<style>
  :root {
    --prussian: #0e4a80;
    --quote-mark: #a3b3cf;
    --frame: #8ea2c3;
    --text: #ffffff;
  }
  * { margin: 0; padding: 0; box-sizing: border-box; }
  html, body { width: 846px; height: 1200px; overflow: hidden; background: var(--prussian); }
  .panel {
    position: relative;
    width: 846px;
    height: 1200px;
    background: var(--prussian);
    overflow: hidden;
  }
  .pattern-field {
    position: absolute;
    left: 0;
    top: 0;
    width: 846px;
    height: 660px;
  }
  .quote {
    position: absolute;
    left: 148px;
    top: 697px;
    width: 640px;
    font-family: "Crimson Text", Georgia, serif;
    font-style: italic;
    font-weight: 400;
    font-size: 46px;
    line-height: 49px;
    color: var(--text);
    white-space: nowrap;
  }
  .quote-line { display: block; }
  .quote-mark {
    position: absolute;
    font-family: "Crimson Text", Georgia, serif;
    font-style: normal;
    font-weight: 700;
    font-size: 180px;
    line-height: 1;
    color: var(--quote-mark);
  }
  .quote-mark--open { left: 58px; top: 650px; }
  .quote-mark--close { left: 632px; top: 772px; }
  .attribution {
    position: absolute;
    left: 148px;
    top: 857px;
    font-family: "Raleway", Arial, sans-serif;
    font-weight: 400;
    font-size: 18px;
    line-height: 1;
    letter-spacing: 2px;
    text-transform: uppercase;
    color: var(--text);
  }
  .brand-frame {
    position: absolute;
    left: 372px;
    top: 938px;
    width: 474px;
    height: 262px;
  }
  .brand {
    position: absolute;
    left: 422px;
    top: 1030px;
    display: flex;
    align-items: center;
    gap: 14px;
  }
  .brand-name {
    font-family: "Raleway", Arial, sans-serif;
    font-weight: 300;
    font-size: 58px;
    line-height: 1;
    color: var(--text);
  }
  .brand-mark {
    width: 24px;
    height: 24px;
    border: 3px solid var(--text);
  }
  .tagline {
    position: absolute;
    left: 424px;
    top: 1104px;
    font-family: "Raleway", Arial, sans-serif;
    font-weight: 400;
    font-size: 13.5px;
    line-height: 1;
    color: var(--text);
  }
</style>
</head>
<body>
  <main class="panel">
    <svg class="pattern-field" role="img" aria-label="Decorative pattern of overlapping nested rounded squares in pale blue" viewBox="0 0 846 660">
      <defs>
        <linearGradient id="patternFade" x1="0" y1="0" x2="1" y2="1">
          <stop offset="0" stop-color="#8fa4c6"/>
          <stop offset="0.55" stop-color="#5f7ea8"/>
          <stop offset="1" stop-color="#2f5a8e"/>
        </linearGradient>
      </defs>
      <path d="M0 0 H690 L700 60 L690 300 L720 330 L720 400 L680 430 L690 500 L650 520 L660 650 L520 650 L500 590 L300 600 L200 580 L0 610 Z" fill="url(#patternFade)" opacity="0.9"/>
    </svg>

    <span class="quote-mark quote-mark--open" aria-hidden="true">“</span>
    <p class="quote">
      <span class="quote-line">The strength of the team is each</span>
      <span class="quote-line">individual member. The strength</span>
      <span class="quote-line">of each member is the team.</span>
    </p>
    <span class="quote-mark quote-mark--close" aria-hidden="true">”</span>
    <p class="attribution">— Dale Harmon</p>

    <svg class="brand-frame" viewBox="0 0 474 262" aria-hidden="true">
      <path d="M6 262 V66 A60 60 0 0 1 66 6 H474" fill="none" stroke="var(--frame)" stroke-width="8"/>
    </svg>
    <div class="brand">
      <span class="brand-name">lumenfold.co</span>
      <span class="brand-mark"></span>
    </div>
    <p class="tagline">Mentoring a lifestyle of art photography and digital media</p>
  </main>
</body>
</html>
```